A5 & A3 Size flyer for OPEN NIGHT - Adult Education

We need a A5 & A3 formatted flyer for our upcoming OPEN NIGHT on Thursday, 17th November 2016 at our Kelmswood campus. A3 for poster to display and A5 for flyers.

We are one of Victoria's leading private Reconised Training Organisations based in Melbourne, Victoria, Australia who specialise in the training of nationally recognised training courses in Pathology, Individual Support (Ageing, Home & Community, Disability), Allied Health Assistance, Health Services Assistance, Disability & Ageing Support.

The purpose of our open night is to gain prospective students for 2017 courses and the soul purpose of this flyer is to promote via emails, postal mail and hard copy drop offs to prospective clients, employers and our partnered networks for exposure.

The final design should reflect the colour scheme & style we have used in the attached already promoted designs. Should include our logo, address, event details, website and social media buttons (Facebook, Instagram, Youtube, Twitter, Pinterest & LinkedIn) Should be in line with our overall branding, as per our website www.brightwellcareskills.edu.au and ensure it is bold and engaging for promotional purposes.

Please also see our event listing for which ahs further information you may be able to use: https://bcsinfoevening16.ticketnook.com.au

If you ahve any questions please send through a message!

Target Market(s)

Prospective students, employer organisations workforce

Industry/Entity Type

Adult

Colors
f37122
f78f20
ffc214
ffffff

Requirements
Must have
• See project description

```html
<!DOCTYPE html>
<html lang="en">
<head>
<meta charset="utf-8">
<title>Open Night 2016 – Brightwell Care Skills</title>
<link rel="stylesheet" href="https://fonts.googleapis.com/css2?family=Questrial&family=Poppins:wght@400;500;600;700&display=swap">
<style>
  :root {
    --orange: #f37122;
    --orange-light: #f78f20;
    --yellow: #ffc214;
    --yellow-bright: #f5d60a;
    --white: #ffffff;
    --maroon: #8a1a10;
    --deep-red: #b3141b;
    --ink: #2a1a10;
    --grey: #9a9a9a;
    --page: #ffffff;
  }
  * { margin: 0; padding: 0; box-sizing: border-box; }
  html, body { width: 1200px; height: 1200px; overflow: hidden; background: var(--page); }
  .flyer {
    position: absolute; left: 182px; top: 16px;
    width: 836px; height: 1168px; overflow: hidden;
    background:
      radial-gradient(ellipse 60% 40% at 100% 100%, var(--white) 0%, rgba(255,255,255,0.9) 35%, rgba(255,255,255,0) 75%),
      linear-gradient(180deg, #d8681e 0%, #b2321a 45%, #e06a1d 58%, var(--orange-light) 66%, var(--yellow) 85%, #ffcf2e 100%);
    font-family: "Poppins", sans-serif;
  }
  .portrait {
    position: absolute; top: 0; height: 400px;
    -webkit-mask-image: linear-gradient(180deg, #000 70%, transparent 100%);
            mask-image: linear-gradient(180deg, #000 70%, transparent 100%);
  }
  .portrait--1 { left: 0; width: 183px; background: linear-gradient(170deg, #c98454, #8a4a2a 60%, #6a2a1a); }
  .portrait--2 { left: 183px; width: 219px; background: linear-gradient(170deg, #e0a46c, #a65a34 55%, #3a2020); }
  .portrait--3 { left: 402px; width: 216px; background: linear-gradient(170deg, #b97a4e, #8c4a2c 55%, #4a2418); }
  .portrait--4 { left: 618px; width: 218px; background: linear-gradient(170deg, #e08a3e, #b65a30 55%, #7a2a18); }
  .courses {
    position: absolute; left: 170px; top: 352px; z-index: 2;
    font-size: 18.5px; font-weight: 500; line-height: 24px; color: var(--white); white-space: nowrap;
  }
  .courses .sep { color: var(--yellow); margin: 0 7px; }
  .headline {
    position: absolute; left: 44px; top: 374px;
    font-family: "Questrial", sans-serif; font-weight: 400; font-size: 148px; line-height: 1;
    letter-spacing: 3px; white-space: nowrap;
  }
  .headline .open { color: var(--yellow-bright); }
  .headline .night { color: #fff3e6; }
  .year {
    position: absolute; left: 204px; top: 494px;
    font-family: "Poppins", sans-serif; font-weight: 600; font-size: 110px; line-height: 1;
    letter-spacing: -5px; color: var(--deep-red);
  }
  .event-date {
    position: absolute; left: 430px; top: 518px;
    font-size: 35px; font-weight: 600; line-height: 44px; color: var(--white); letter-spacing: -0.5px; white-space: nowrap;
  }
  .event-venue {
    position: absolute; left: 434px; top: 562px;
    font-size: 21px; font-weight: 500; line-height: 26px; color: var(--yellow); white-space: nowrap;
  }
  .intro {
    position: absolute; left: 205px; top: 608px;
    font-size: 15.6px; font-weight: 600; line-height: 18px; color: var(--maroon); white-space: nowrap;
  }
  .prize-image {
    position: absolute; left: 0; top: 508px; width: 186px; height: 134px;
    background: linear-gradient(150deg, #e8eef2, #6a9ac8 45%, #d9dde2);
    clip-path: polygon(0 10%, 30% 0, 100% 70%, 70% 100%, 0 55%);
  }
  .prize-note {
    position: absolute; left: 20px; top: 680px; width: 180px;
    font-size: 18px; font-weight: 500; line-height: 20px; color: var(--white); text-align: center;
  }
  .students-photo {
    position: absolute; left: 90px; top: 708px; width: 520px; height: 460px;
    background: radial-gradient(ellipse 55% 50% at 50% 45%, rgba(200,110,60,0.85), rgba(247,143,32,0.4) 60%, rgba(255,194,20,0) 100%);
  }
  .brand {
    position: absolute; left: 620px; top: 790px; width: 176px; text-align: center;
  }
  .brand-mark {
    width: 120px; height: 120px; margin: 0 auto 48px; border-radius: 50%;
    background: var(--orange);
  }
  .brand-name {
    font-family: "Questrial", sans-serif; font-size: 31px; line-height: 33px;
    color: var(--orange); letter-spacing: 1px;
  }
  .toid {
    position: absolute; left: 620px; top: 1046px; width: 176px; text-align: center;
    font-family: "Questrial", sans-serif; font-size: 16px; color: var(--grey);
  }
  .tagline {
    position: absolute; left: 46px; top: 1032px;
    font-family: "Questrial", sans-serif; font-size: 32px; line-height: 36px; color: rgba(200,110,40,0.75); white-space: nowrap;
  }
  .contact-line {
    position: absolute; left: 50px; top: 1074px;
    display: flex; align-items: center; gap: 6px;
    font-size: 20px; font-weight: 600; color: var(--ink); white-space: nowrap;
  }
  .contact-line svg { width: 30px; height: 30px; }
  .address {
    position: absolute; left: 50px; top: 1102px;
    font-size: 20px; color: var(--ink); white-space: nowrap;
  }
  .social {
    position: absolute; left: 622px; top: 1096px; display: flex; gap: 8px;
  }
  .social span { width: 28px; height: 28px; background: var(--orange); display: block; }
</style>
</head>
<body>
  <main class="flyer">
    <div class="portrait portrait--1" role="img" aria-label="Portrait photo of a smiling male student"></div>
    <div class="portrait portrait--2" role="img" aria-label="Portrait photo of a smiling young female student"></div>
    <div class="portrait portrait--3" role="img" aria-label="Portrait photo of a smiling female student"></div>
    <div class="portrait portrait--4" role="img" aria-label="Portrait photo of a smiling older female student"></div>

    <h1 class="headline"><span class="open">Open</span><span class="night">Night</span></h1>
    <p class="courses">Pathology<span class="sep">|</span>Aged CAre<span class="sep">|</span>Disability<span class="sep">|</span>Allied Health<span class="sep">|</span>Heath Services</p>
    <p class="year">2016</p>
    <p class="event-date">17 November 5-8pm</p>
    <p class="event-venue">Brightwell Care Skills Kelmswood</p>

    <p class="intro">Looking for a career change? Not sure what to do once high school<br>has finished? Or simply wanting to UpSkill? Come along and join us at<br>our Open Night – explore our campus, get all your questions answered<br>and learn what career and course options are available to you in 2017.</p>

    <div class="prize-image" role="img" aria-label="Photo of a tablet computer prize"></div>
    <p class="prize-note">Slate Mini and<br>other prizes<br>must be won</p>

    <div class="students-photo" role="img" aria-label="Photo of two female students smiling in class"></div>

    <div class="brand">
      <div class="brand-mark"></div>
      <p class="brand-name">brightwell care skills</p>
    </div>
    <p class="toid">TOID No. 40918</p>

    <p class="tagline">Making you the future of healthcare</p>
    <p class="contact-line">www.brightwellcareskills.edu.au
      <svg viewBox="0 0 30 30" aria-hidden="true">
        <circle cx="15" cy="15" r="15" fill="var(--orange)"/>
        <path d="M10 8c1-1 2-1 3 0l1.5 2.5c.5 1 0 1.7-.7 2.3-.6.5-.5 1 .2 2l1.5 1.8c.8.8 1.3.8 1.9.1.6-.7 1.3-1.2 2.3-.6L22 17.6c1 .8 1 1.9 0 2.8-1.8 1.8-4.6 1.2-7.8-2-3.4-3.3-5.9-7.8-4.2-10.4z" fill="var(--white)"/>
      </svg>
      03 9000 4127</p>
    <p class="address">Level 2, 14 Station Parade, Kelmswood VIC 3199</p>

    <div class="social" aria-label="Social media links">
      <span></span><span></span><span></span><span></span><span></span>
    </div>
  </main>
</body>
</html>
```